Lumora Vitality MediSpa Brochure

We need a new brochure design. The old is attached.

We are wanting a three panel brochure for med spa designed and ready for print. The brochure will have content and images on both sides. We attached the old brochure in pdf format. The content needs to stay as on the attached pdf but please feel free to offer new designs. The color needs to match the attached logo, which is a light blue and teal. All images we want on the brochure are also attached.

The design must have an 1/8 in space from each edge for printing purposes

Target Market(s)

Men and Women

Industry/Entity Type

Wellness

Font styles to use
Sans Serif

Colors
34a6d7
33b8a4

Requirements
Must have
• soft curves. must have a 1/8 in space on all edges (including interior) to give bleed space for printing. Use content written on attached brochure.

```html
<!DOCTYPE html>
<html lang="en">
<head>
<meta charset="utf-8">
<title>Lumora Vitality MediSpa – Tri-fold Brochure</title>
<link rel="stylesheet" href="https://fonts.googleapis.com/css2?family=Tenor+Sans&family=Nunito+Sans:wght@400;700;800&display=swap">
<style>
  :root{
    --bg:#2b2b2d;
    --teal:#22a3a3;
    --teal-dark:#0d6d72;
    --teal-mid:#1a8a8d;
    --sky:#34a6d7;
    --white:#ffffff;
    --ink:#2f3f44;
    --heading:#0f5f66;
    --photo-a:#e9d6cb;
    --photo-b:#9cb5b8;
    --portrait-a:#6f8f55;
    --portrait-b:#3b4a66;
  }
  *{box-sizing:border-box;margin:0;padding:0}
  html,body{width:1200px;height:800px;overflow:hidden;background:var(--bg)}
  body{font-family:"Nunito Sans",sans-serif;color:var(--ink)}
  .brochure{position:absolute;left:45px;top:40px;width:1110px;height:720px;display:flex;box-shadow:0 12px 40px rgba(0,0,0,.5)}
  .panel{position:relative;width:370px;height:720px;overflow:hidden;background:var(--white)}
  .panel + .panel{border-left:1px solid rgba(0,0,0,.08)}
  .panel-bg{position:absolute;inset:0;width:100%;height:100%}
  .display{font-family:"Tenor Sans",sans-serif;letter-spacing:.5px}
  .strong{font-weight:800;letter-spacing:.6px}
  .body-copy{font-size:12.5px;line-height:1.45}
  .on-teal{color:var(--white)}
  .tick-list{list-style:none}
  .tick-list li{display:flex;align-items:center;gap:7px;font-size:12.5px;line-height:1.55}
  .tick-list svg{width:11px;height:11px;flex:none}
  .contact{display:flex;align-items:center;gap:8px;font-size:13px;line-height:1.6}
  .contact svg{width:13px;height:13px;flex:none}
  .contact.phone{font-weight:800;font-size:15px}
  .contact.web{font-size:12px}

  /* panel: about */
  .about-title{position:absolute;left:40px;right:30px;top:52px;text-align:right;color:var(--heading)}
  .about-title .display{font-size:20px}
  .about-title .strong{font-size:19px}
  .about-text{position:absolute;left:40px;right:34px;top:115px;text-align:right}
  .why-title{position:absolute;left:40px;right:34px;top:220px;text-align:right;color:var(--heading)}
  .why-title .display{font-size:19px}
  .why-title .strong{font-size:19px}
  .why-text{position:absolute;left:60px;right:34px;top:276px;text-align:right}
  .why-text p + p{margin-top:10px}
  .member{position:absolute;left:34px;right:30px;top:492px}
  .member .display{font-size:18px}
  .member .strong{font-size:17px;margin-bottom:8px}
  .member .body-copy{margin-bottom:6px;font-size:12px}
  .member .tick-list li{font-weight:800;font-size:12px;line-height:1.45}
  .member-contact{position:absolute;left:34px;bottom:20px}

  /* panel: physician */
  .doc-title{position:absolute;left:28px;top:34px;color:var(--heading)}
  .doc-title .strong{font-size:18px}
  .doc-title .display{font-size:15px}
  .portrait{position:absolute;left:240px;top:76px;width:104px;height:104px;border-radius:50%;background:radial-gradient(circle at 50% 40%,var(--portrait-a),var(--portrait-b));border:5px solid var(--white);box-shadow:0 0 0 5px var(--teal)}
  .quotes{position:absolute;left:28px;right:30px;top:115px;font-size:12px;line-height:1.4}
  .quotes p + p{margin-top:12px}
  .quotes .q1{width:170px}
  .quotes .q3{width:215px}
  .visit{position:absolute;left:0;right:0;top:478px;text-align:center}
  .visit .pin{width:28px;height:28px;margin:0 auto 6px}
  .visit .address{font-size:13.5px;line-height:1.35}
  .cta{display:inline-block;margin:12px auto 10px;padding:7px 24px;border-radius:20px;background:var(--teal-dark);font-weight:800;font-size:13.5px;letter-spacing:.5px;box-shadow:inset 0 2px 0 rgba(255,255,255,.2)}
  .visit .contact{justify-content:center;font-weight:800;font-size:14px;line-height:1.5}
  .visit .contact.small{font-weight:400;font-size:12px}

  /* panel: cover */
  .brand{position:absolute;left:0;right:0;top:36px;text-align:center;font-family:"Tenor Sans",sans-serif;color:var(--teal-mid);font-size:21px;letter-spacing:1px}
  .brand-mark{display:inline-block;width:12px;height:12px;border-radius:50%;background:var(--sky);margin-right:8px;vertical-align:middle}
  .hero{position:absolute;left:40px;top:95px;width:290px;height:290px;border-radius:50%;background:radial-gradient(circle at 55% 45%,var(--photo-a),var(--photo-b));border:7px solid var(--white);box-shadow:0 0 0 7px var(--teal)}
  .hero-sketch{position:absolute;left:272px;top:392px;width:86px;height:112px;border-radius:45% 45% 40% 40%;background:rgba(255,255,255,.18)}
  .cover-title{position:absolute;left:30px;top:462px}
  .cover-title .display{font-size:26px}
  .cover-title .strong{font-size:17px;margin-bottom:8px}
  .cover-title .tick-list li{font-size:12.5px}
  .audience{position:absolute;right:24px;top:520px;text-align:right;font-weight:800;font-size:19px;line-height:1.05;color:var(--heading)}
  .cover-contact{position:absolute;left:30px;bottom:20px}
</style>
</head>
<body>
<main class="brochure">

  <!-- panel 1: about & memberships -->
  <section class="panel panel-about">
    <svg class="panel-bg" viewBox="0 0 370 720" preserveAspectRatio="none" aria-hidden="true">
      <rect width="370" height="720" fill="var(--teal)"/>
      <path d="M70 0 H370 V440 C320 490 200 500 120 468 C50 440 0 410 0 370 V130 C0 60 30 20 70 0 Z" fill="var(--white)"/>
      <path d="M0 392 C60 470 210 508 370 458" fill="none" stroke="var(--teal-dark)" stroke-width="6"/>
      <path d="M0 130 C10 60 40 20 70 0" fill="none" stroke="var(--teal-dark)" stroke-width="5"/>
    </svg>
    <h2 class="about-title"><div class="display">BROOKHAVEN'S</div><div class="strong">PREMIER MEDISPA</div></h2>
    <p class="about-text body-copy">Lumora Vitality MediSpa is the premier medical spa in Brookhaven, TX. We utilize the best equipment available today for laser treatments, dermal fillers, facials, injections, chemical peels and wellness solutions.</p>
    <h2 class="why-title"><div class="display">WHY CHOOSE OUR</div><div class="strong">MEDISPA?</div></h2>
    <div class="why-text body-copy">
      <p>Under the supervision of Dr. Elena Hartwell, our medical staff provides state-of-the-art cosmetic treatments to both women and men.</p>
      <p>Our staff is trained to provide unique medicalspa services to help our clients achieve a more youthful look and defy the aging process.</p>
    </div>
    <div class="member on-teal">
      <div class="display">EXCLUSIVE</div>
      <div class="strong">MEMBERSHIPS</div>
      <p class="body-copy">Our exclusive membership packages are tailored for our clients and created to give them an exceptional experience at a discounted price.</p>
      <ul class="tick-list">
        <li><svg viewBox="0 0 12 12"><path d="M1 6 L4.5 9.5 L11 2" fill="none" stroke="#fff" stroke-width="2"/></svg>SILVER Membership</li>
        <li><svg viewBox="0 0 12 12"><path d="M1 6 L4.5 9.5 L11 2" fill="none" stroke="#fff" stroke-width="2"/></svg>GOLD Membership</li>
        <li><svg viewBox="0 0 12 12"><path d="M1 6 L4.5 9.5 L11 2" fill="none" stroke="#fff" stroke-width="2"/></svg>PLATINUM Membership</li>
      </ul>
    </div>
    <div class="member-contact on-teal">
      <div class="contact phone"><svg viewBox="0 0 14 14"><circle cx="7" cy="7" r="6.2" fill="none" stroke="#fff" stroke-width="1.3"/><path d="M4.5 4 C4.5 7.5 6.5 9.5 10 9.5 L10 8.3 L8.6 7.8 L8 8.4 C7 8 6 7 5.6 6 L6.2 5.4 L5.7 4 Z" fill="#fff"/></svg>(555) 014-3016</div>
      <div class="contact web"><svg viewBox="0 0 14 14"><circle cx="7" cy="7" r="6" fill="none" stroke="#fff" stroke-width="1.2"/><path d="M1 7 H13 M7 1 C4 4 4 10 7 13 M7 1 C10 4 10 10 7 13" fill="none" stroke="#fff" stroke-width="1"/></svg>www.LumoraVitalityMedispa.com</div>
    </div>
  </section>

  <!-- panel 2: physician & contact -->
  <section class="panel panel-doctor">
    <svg class="panel-bg" viewBox="0 0 370 720" preserveAspectRatio="none" aria-hidden="true">
      <rect width="370" height="720" fill="var(--white)"/>
      <path d="M210 0 H370 V270 C340 215 310 195 270 198 C320 160 320 60 210 0 Z" fill="var(--teal)"/>
      <path d="M0 720 V490 C60 490 150 460 185 390 C220 460 300 510 370 490 V720 Z" fill="var(--teal)"/>
      <path d="M0 480 C60 480 150 450 185 380" fill="none" stroke="var(--teal-dark)" stroke-width="5"/>
    </svg>
    <h2 class="doc-title"><div class="strong">DR. ELENA HARTWELL</div><div class="display">MD FACS</div></h2>
    <div class="portrait" role="img" aria-label="Portrait photo of Dr. Elena Hartwell"></div>
    <div class="quotes">
      <p class="q1">"Rejuvenation and reconstruction of the face are my passion, whether it is to improve one's visual functions or to enhance one's appearance."</p>
      <p>"I personally perform all of my injections and CO2 laser treatments because safety and satisfaction are my top priorities."</p>
      <p class="q3">"I was called by God to become a physician at the age of seven years old. I am motivated by a desire to serve others by providing superb medical care. I constantly strive to do my best."</p>
    </div>
    <div class="visit on-teal">
      <svg class="pin" viewBox="0 0 28 28"><circle cx="14" cy="14" r="13" fill="var(--white)"/><path d="M14 6 C10.5 6 9 8.5 9 10.8 C9 14.5 14 20 14 20 C14 20 19 14.5 19 10.8 C19 8.5 17.5 6 14 6 Z" fill="var(--teal-dark)"/><circle cx="14" cy="11" r="2" fill="var(--white)"/></svg>
      <p class="address">418 W. Meadowbrook Blvd<br>Suite 210<br>Brookhaven TX 75400</p>
      <div class="cta">SCHEDULE A CONSULTATION</div>
      <div class="contact"><svg viewBox="0 0 14 14"><circle cx="7" cy="7" r="6.2" fill="none" stroke="#fff" stroke-width="1.3"/><path d="M4.5 4 C4.5 7.5 6.5 9.5 10 9.5 L10 8.3 L8.6 7.8 L8 8.4 C7 8 6 7 5.6 6 L6.2 5.4 L5.7 4 Z" fill="#fff"/></svg>(555) 014-5015</div>
      <div class="contact"><svg viewBox="0 0 14 14"><rect x="2" y="5" width="10" height="6" rx="1" fill="#fff"/><rect x="4" y="2" width="6" height="3" fill="#fff"/></svg>(555) 019-6565</div>
      <div class="contact small"><svg viewBox="0 0 14 14"><rect x="1.5" y="3" width="11" height="8" fill="none" stroke="#fff" stroke-width="1.2"/><path d="M1.5 3 L7 8 L12.5 3" fill="none" stroke="#fff" stroke-width="1.2"/></svg>glow@elenahartwellmd.com</div>
      <div class="contact small"><svg viewBox="0 0 14 14"><circle cx="7" cy="7" r="6" fill="none" stroke="#fff" stroke-width="1.2"/><path d="M1 7 H13 M7 1 C4 4 4 10 7 13 M7 1 C10 4 10 10 7 13" fill="none" stroke="#fff" stroke-width="1"/></svg>www.LumoraVitalityMedispa.com</div>
    </div>
  </section>

  <!-- panel 3: cover -->
  <section class="panel panel-cover">
    <svg class="panel-bg" viewBox="0 0 370 720" preserveAspectRatio="none" aria-hidden="true">
      <rect width="370" height="720" fill="var(--white)"/>
      <path d="M0 720 V300 C30 400 110 450 200 440 C280 430 340 420 370 380 V720 Z" fill="var(--teal)"/>
      <path d="M0 290 C30 390 110 440 200 430 C280 420 340 410 370 370" fill="none" stroke="var(--teal-dark)" stroke-width="5"/>
      <path d="M310 720 C335 650 370 615 370 615 V720 Z" fill="var(--white)" opacity=".9"/>
    </svg>
    <div class="brand"><span class="brand-mark"></span>Lumora Vitality MediSpa</div>
    <div class="hero" role="img" aria-label="Close-up photo of a woman's smooth, glowing skin"></div>
    <div class="hero-sketch" role="img" aria-label="Faint line illustration of a woman's profile"></div>
    <div class="cover-title on-teal">
      <div class="display">REFRESH</div>
      <div class="strong">AND REJUVENATE</div>
      <ul class="tick-list">
        <li><svg viewBox="0 0 12 12"><path d="M1 6 L4.5 9.5 L11 2" fill="none" stroke="#fff" stroke-width="2"/></svg>Laser Treatments</li>
        <li><svg viewBox="0 0 12 12"><path d="M1 6 L4.5 9.5 L11 2" fill="none" stroke="#fff" stroke-width="2"/></svg>Dermal Fillers</li>
        <li><svg viewBox="0 0 12 12"><path d="M1 6 L4.5 9.5 L11 2" fill="none" stroke="#fff" stroke-width="2"/></svg>Neurotoxins</li>
        <li><svg viewBox="0 0 12 12"><path d="M1 6 L4.5 9.5 L11 2" fill="none" stroke="#fff" stroke-width="2"/></svg>Facials</li>
        <li><svg viewBox="0 0 12 12"><path d="M1 6 L4.5 9.5 L11 2" fill="none" stroke="#fff" stroke-width="2"/></svg>Chemical Peels</li>
        <li><svg viewBox="0 0 12 12"><path d="M1 6 L4.5 9.5 L11 2" fill="none" stroke="#fff" stroke-width="2"/></svg>Wellness Treatments</li>
      </ul>
    </div>
    <div class="audience">FOR<br>WOMEN<br>&amp; MEN</div>
    <div class="cover-contact on-teal">
      <div class="contact phone"><svg viewBox="0 0 14 14"><circle cx="7" cy="7" r="6.2" fill="none" stroke="#fff" stroke-width="1.3"/><path d="M4.5 4 C4.5 7.5 6.5 9.5 10 9.5 L10 8.3 L8.6 7.8 L8 8.4 C7 8 6 7 5.6 6 L6.2 5.4 L5.7 4 Z" fill="#fff"/></svg>(555) 014-3016</div>
      <div class="contact web"><svg viewBox="0 0 14 14"><circle cx="7" cy="7" r="6" fill="none" stroke="#fff" stroke-width="1.2"/><path d="M1 7 H13 M7 1 C4 4 4 10 7 13 M7 1 C10 4 10 10 7 13" fill="none" stroke="#fff" stroke-width="1"/></svg>www.LumoraVitalityMedispa.com</div>
    </div>
  </section>

</main>
</body>
</html>
```